Flyer-Design für landwirtschaftlichen Betrieb
Zielgruppe
Wir sind ein landwirtschaftlicher Betrieb mit Ziegenhaltung und Direktvermarktung sowie einer Hofkäserei in der wir unsere Milch zu handwerklich hergestellten Ziegenkäsen (Frischkäse, Weichkäse, Schnittkäse) verarbeiten.
Ziegenrohmilch, Wurst und Ziegenfleisch runden das Angebot ab.
Käseproben sind ebenfalls buchbar.
Im Hofladen gibt es darüber hinaus noch weitere Produkte wie Eier, Obst, Gemüse, Nudeln,...von benachbarten Betrieben.
Der Verkauf läuft über SB Automaten täglich (auch Sonn,- und Feiertage) ab 7 Uhr.
Wir sind ein moderner, gläserner Familienbetrieb und die Kunden haben jederzeit die Möglichkeit zu sehen wo ihr Lebensmittel herkommt.
Unsere Zielgruppe sind vorwiegend Familien.
Aufgabenstellung
Wir wünschen uns ein modernes Design was jedoch den landwirtschaftlichen Aspekt wiedergibt.
Das Herzstück unseres Betriebes ist die Hofkäserei.
Je nach Platzbedarf würden wir gerne eine Anfahrtsskizze auf dem Flyer haben, sowie einen Facebook Hinweis.
Unser Logo ist den Bilddateien beigefügt. Diese können gerne benutzt werden, ebenso wie Stockmaterial.

```html
<!DOCTYPE html>
<html lang="de">
<head>
<meta charset="utf-8">
<title>Ziegenhof Lindenau – Flyer</title>
<link href="https://fonts.googleapis.com/css2?family=Hind:wght@300;400;600&family=Satisfy&display=block" rel="stylesheet">
<style>
  :root{
    --stage:#ececec;
    --green:#0f9a47;
    --green-deep:#0b8a3e;
    --meadow-haze:#8e9a8c;
    --meadow-light:#95ad7a;
    --meadow-mid:#6c8b4c;
    --meadow-dark:#48692f;
    --brown:#5a3525;
    --white:#ffffff;
    --text:#ffffff;
  }
  *{box-sizing:border-box;margin:0;padding:0}
  html,body{width:1200px;height:900px;overflow:hidden;background:var(--stage)}
  body{position:relative;font-family:"Hind",sans-serif;color:var(--text)}

  .page{position:absolute;top:68px;width:528px;height:744px;overflow:hidden;box-shadow:0 14px 22px -12px rgba(0,0,0,.35)}
  .page--front{left:46px}
  .page--back{left:624px}

  .photo-bg{position:absolute;inset:0}
  .page--front .photo-bg{background:
      radial-gradient(ellipse 60% 30% at 70% 55%,rgba(170,180,110,.55),rgba(170,180,110,0)),
      linear-gradient(180deg,var(--meadow-haze) 0%,#8b9b83 22%,var(--meadow-light) 42%,var(--meadow-mid) 68%,var(--meadow-dark) 100%)}
  .page--back .photo-bg{background:
      radial-gradient(ellipse 50% 35% at 30% 60%,rgba(140,165,100,.5),rgba(140,165,100,0)),
      linear-gradient(180deg,#5d7b45 0%,var(--meadow-mid) 40%,#7a965c 65%,#587a3c 100%)}

  .goat-photo{position:absolute}
  .page--front .goat-photo{left:0;top:30px;width:215px;height:714px;
      background:radial-gradient(ellipse 75% 55% at 45% 42%,#f4f1ea 0%,#e6e0d4 45%,#cfc8b9 65%,rgba(190,185,170,0) 85%)}
  .page--back .goat-photo{left:318px;top:190px;width:210px;height:370px;
      background:radial-gradient(ellipse 70% 55% at 62% 45%,#e4d2bb 0%,#c8ab8a 45%,#a88c6c 65%,rgba(140,120,90,0) 88%)}

  .grass-band{position:absolute;left:0;right:0;bottom:0;height:200px;
      background:linear-gradient(180deg,rgba(15,154,71,0) 0%,rgba(15,154,71,.55) 35%,var(--green) 62%,var(--green-deep) 100%)}

  .brand-box{position:absolute;top:0;left:346px;width:152px;height:197px;background:var(--white);
      display:flex;flex-direction:column;align-items:center;justify-content:center;gap:14px;box-shadow:0 2px 8px rgba(0,0,0,.25)}
  .brand-box .dot{width:82px;height:82px;border-radius:50%;background:var(--green)}
  .brand-box .name{font-weight:600;font-size:17px;color:var(--brown);text-align:center;line-height:1.1}

  .script{font-family:"Satisfy",cursive;font-weight:400;text-shadow:0 1px 3px rgba(0,0,0,.4)}

  .front-copy h2{position:absolute;left:233px;font-size:32px;line-height:1;white-space:nowrap}
  .front-copy .txt{position:absolute;left:233px;width:290px;font-weight:300;font-size:16px;line-height:21.5px;text-shadow:0 1px 2px rgba(0,0,0,.25)}
  .front-copy ul{list-style:none}
  .front-copy li{position:relative;padding-left:16px;margin-bottom:5px}
  .front-copy li::before{content:"•";position:absolute;left:0}
  .h-kaese{top:228px}.t-kaese{top:262px}
  .h-regio{top:399px}.t-regio{top:437px}
  .h-sb{top:474px}.t-sb{top:503px}
  .h-probe{top:560px}

  .footer-line{position:absolute;left:30px;top:684px;font-size:14.5px;font-weight:400;white-space:nowrap}
  .footer-line .script{font-size:22px;margin-right:1px;text-shadow:none}

  .herd-photo{position:absolute;left:40px;top:40px;width:285px;height:158px;
      background:linear-gradient(90deg,#5b3f2b 0%,#8c6a4d 18%,#e7e0d5 30%,#f1ece3 50%,#ddd4c6 70%,#6d4c35 85%,#4a3222 100%)}

  .about{position:absolute;left:38px;top:210px;width:290px}
  .about h2{font-size:30px;line-height:1.1;margin-bottom:6px;white-space:nowrap}
  .about p{font-weight:300;font-size:15px;line-height:21.4px;margin-bottom:5px;text-shadow:0 1px 2px rgba(0,0,0,.25)}
  .about strong{font-weight:600}

  .contact{position:absolute;left:38px;top:532px;width:210px;font-weight:300;font-size:15px;line-height:19px}
  .contact .title{font-weight:400;margin-bottom:4px;white-space:nowrap}
  .contact .title .script{font-size:25px;text-shadow:none}
  .contact .web{margin-top:7px}
  .contact .social{display:flex;align-items:center;gap:6px;margin-top:5px}
  .contact .social i{display:block;width:16px;height:16px;border-radius:3px;background:var(--white)}

  .map{position:absolute;left:244px;top:523px;width:253px;height:171px;
      background:linear-gradient(135deg,#ffffff 0%,#f7f1ec 45%,#efe4dc 70%,#e6efe4 100%);box-shadow:0 3px 8px rgba(0,0,0,.3)}
</style>
</head>
<body>
  <section class="page page--front">
    <div class="photo-bg" role="img" aria-label="Unscharfe Wiese als Hintergrundfoto"></div>
    <div class="goat-photo" role="img" aria-label="Foto einer weißen Ziege mit Hörnern"></div>
    <div class="grass-band" role="img" aria-label="Grashalme auf grünem Band"></div>
    <div class="brand-box"><span class="dot"></span><span class="name">Ziegenhof<br>Lindenau</span></div>
    <div class="front-copy">
      <h2 class="script h-kaese">Hofkäserei</h2>
      <div class="txt t-kaese">
        <p>mit eigener Herstellung</p>
        <ul style="margin-top:6px">
          <li>Ziegenkäse:<br>Frischkäse, Weichkäse, Schnittkäse</li>
          <li>Ziegenrohmilch</li>
          <li>Ziegenfleisch, -wurst</li>
        </ul>
      </div>
      <h2 class="script h-regio">Regionale Produkte</h2>
      <div class="txt t-regio"><ul><li>Eier, Obst, Gemüse, Nudeln u.v.m.</li></ul></div>
      <h2 class="script h-sb">SB-Automat</h2>
      <div class="txt t-sb"><p>täglich ab 7 Uhr<br>(auch Sonn,- und Feiertage)</p></div>
      <h2 class="script h-probe">Käseproben</h2>
    </div>
    <div class="footer-line"><span class="script">Ziegenhof</span>Lindenau: Lindenweg 1, 77999 Talheim-Au</div>
  </section>

  <section class="page page--back">
    <div class="photo-bg" role="img" aria-label="Wiese mit Gräsern als Hintergrundfoto"></div>
    <div class="goat-photo" role="img" aria-label="Foto einer braun-weißen Ziege im Gras"></div>
    <div class="grass-band" role="img" aria-label="Grashalme auf grünem Band"></div>
    <div class="herd-photo" role="img" aria-label="Foto mehrerer weißer Ziegen auf einem Holzsteg im Stall"></div>
    <div class="brand-box"><span class="dot"></span><span class="name">Ziegenhof<br>Lindenau</span></div>
    <div class="about">
      <h2 class="script">Lernen Sie uns kennen!</h2>
      <p>Wir sind ein landwirtschaftlicher Vollerwerbsbetrieb mit den Bereichen <strong>Tierhaltung, Ackerbau und Ziegen-Direktvermarktung.</strong> Wir beschäftigen uns intensiv mit der Ziegenhaltung, bieten hochwertige Ziegenprodukte und regionale Lebensmittel an.</p>
      <p>Kommen Sie uns besuchen und lernen Sie unseren modernen, gläsernen Familienbetrieb kennen und sehen Sie, wo Ihre Lebensmittel herkommen.</p>
    </div>
    <div class="contact">
      <div class="title"><span class="script">Ziegenhof</span> Lindenau</div>
      <div>Lindenweg 1<br>77999 Talheim-Au<br>Telefon: 07 12 3 / 456</div>
      <div class="web">www.ziegenhof-lindenau.de</div>
      <div class="social"><i></i>Ziegenhof Lindenau</div>
    </div>
    <div class="map" role="img" aria-label="Anfahrtsskizze mit Straßen, Autobahn und Markierung des Hofes"></div>
  </section>
</body>
</html>
```